Diesel Trailer Manufacturer Website Design

We are working with a Trailer Manufacturer in Texas. They provide custom-made trailers for diesel trucks throughout the US.
Some sites to use for content/competitors:
www.birchhaulers.com
https://velmotrailers.com
http://www.dunhollowcustomtrailers.com/
https://www.pellingtrailer.com
https://www.roadwren.com
Thank you for taking the time to consider designing a website for us. We are web developers based in Stockton, CA, USA. Most of our projects go through the same process. Understanding this process may help you win a project with us. We custom-code all of our websites in-house. We don’t have any requirements as to what tools you use for your design, but we ask that you follow these guidelines.
IMAGES:
If you use any images or icons in the design, we ask that you have a link to the asset so we can purchase the image/icon. Most of the designs we submit do not have the customer’s images on them unless they have some great images. Be creative; show us the feeling you are trying to portray with your image choices. Use any royalty-free site you choose. We subscribe to Quillor and mainly use their images, but we can purchase images outside of Quillor. PLEASE NOTE: we will not submit designs to clients with watermarks on the images.
FONTS:
We ask that you identify the fonts you’re using in the design. This can be done in a message if you want. We typically use Fennix Fonts and Quillor Fonts.
CONTENT:
We're always open to different content and ideas. We often submit designs with stock images so the client can see our vision. We typically take pictures after the website launch to use their images with our vision. Lorem Ipsum is fine for paragraphs, but we ask that you make the Headers with correct English. We want to be able to show the vision and identify the sections of the website.
INSPIRATION:
We typically add a couple of links in the brief of websites we like to help you get started in your design.
REVISIONS:
We do not often ask for revisions of the designs unless we see something in the design that may not appeal to the client. If there are slight changes that we want to make, we do that in the development process.
FEEDBACK:
We rarely give feedback on designs during the design process. We are working on many website projects and do not have the time to provide feedback. We usually respond if your request is well thought out and asks specific questions, but a note asking “feedback, please” usually goes unanswered.
1 page

```html
<!DOCTYPE html>
<html lang="en">
<head>
<meta charset="utf-8">
<title>Keystone Haul – Custom Trailers</title>
<link href="https://fonts.googleapis.com/css2?family=Crimson+Text:wght@400;700&family=Kumbh+Sans:wght@400;500;600;700&display=swap" rel="stylesheet">
<style>
:root{
  --red:#8b0000;
  --red-bright:#b3111a;
  --ink:#1f1f1f;
  --muted:#444;
  --panel:#f4f4f4;
  --white:#fff;
  --footer:#1b1b1b;
  --gold:#f0a500;
  --line:#d9d9d9;
}
*{box-sizing:border-box;margin:0;padding:0}
html,body{width:1200px;height:4773px;overflow:hidden}
body{position:relative;background:var(--white);font-family:"Kumbh Sans",sans-serif;color:var(--ink)}
.abs{position:absolute}
.serif{font-family:"Crimson Text",serif}
h2.section-title{position:absolute;font-family:"Crimson Text",serif;font-weight:400;font-size:50px;line-height:1;color:var(--ink)}
h2.section-title b{color:var(--red);font-weight:700}
p.body{font-size:12.5px;line-height:25px;color:var(--ink)}
.btn{position:absolute;background:var(--red);color:#fff;font-size:13px;display:flex;align-items:center;justify-content:center;box-shadow:4px 0 0 #fff,7px 0 0 var(--red),10px 0 0 #fff,12px 0 0 var(--red)}
.photo{position:absolute}

/* top bar */
.topbar{position:absolute;left:0;top:0;width:1200px;height:52px;background:var(--red);color:#fff;font-size:10px}
.social{position:absolute;width:30px;height:30px;border-radius:50%;background:#fff}
/* nav */
.nav a{position:absolute;top:82px;font-size:13px;color:var(--ink);text-decoration:none}
.nav a.active{color:var(--red);font-weight:600}
.logo-box{position:absolute;left:506px;top:0;width:189px;height:144px;background:#fff;box-shadow:0 6px 14px rgba(0,0,0,.18);display:flex;flex-direction:column;align-items:center;justify-content:center;gap:10px}
.logo-box .mark{width:26px;height:26px;background:var(--red)}
.logo-box .name{font-family:"Crimson Text",serif;font-weight:700;font-size:24px;color:var(--red)}

/* hero */
.hero{position:absolute;left:0;top:130px;width:1200px;height:598px;background:var(--panel)}
.hero h1{position:absolute;left:120px;top:138px;font-family:"Crimson Text",serif;font-weight:400;font-size:52px;line-height:49px;color:var(--ink)}
.hero h1 b{color:var(--red);font-weight:700}

/* why */
.bar-row{position:absolute;left:120px;width:445px;font-size:12.5px}
.bar-row .track{position:absolute;left:0;top:36px;width:445px;height:2px;background:var(--line)}
.bar-row .fill{position:absolute;left:0;top:36px;height:2px;background:var(--red)}
.bar-row .dot{position:absolute;top:32px;width:10px;height:10px;border-radius:50%;background:var(--red)}
.bar-row .val{position:absolute;top:0;color:var(--red);font-size:15px}

/* cards */
.trailer-card{position:absolute;top:2321px;width:304px;height:313px;background:#fff}
.t-card{position:absolute;top:2991px;width:450px;height:183px;background:#fff;box-shadow:0 6px 18px rgba(0,0,0,.06)}
.t-card p{position:absolute;left:56px;top:48px;width:340px;font-size:11px;line-height:23px;color:#333}
.t-card .who{position:absolute;right:52px;top:141px;font-size:11px;letter-spacing:2px;font-weight:700}
.t-card .avatar{position:absolute;left:56px;top:135px;width:74px;height:74px;border-radius:50%}
.t-card .quote{position:absolute;right:74px;top:-22px;font-family:"Crimson Text",serif;font-weight:700;font-size:96px;line-height:1;color:var(--red)}

.blog-card{position:absolute;top:3517px;width:306px;height:424px;background:#fff;text-align:center}
.blog-card .img{position:absolute;left:19px;top:0;width:268px;height:189px}
.blog-card .date{position:absolute;left:0;right:0;top:222px;font-size:12px;color:#555}
.blog-card h3{position:absolute;left:30px;right:30px;top:247px;font-size:16px;font-weight:400;line-height:20px}
.blog-card p{position:absolute;left:40px;right:40px;top:298px;font-size:11.5px;line-height:23px;color:#555}
.blog-card .more{position:absolute;left:0;right:0;top:376px;font-size:12px;color:var(--gold)}

/* footer */
.footer{position:absolute;left:0;top:4052px;width:1200px;height:721px;background:var(--footer);color:#fff}
.footer h4{position:absolute;top:333px;font-family:"Crimson Text",serif;font-weight:700;font-size:25px}
.footer .divider{position:absolute;top:368px;width:1px;height:149px;background:#777}
.footer ul{list-style:none;position:absolute;left:533px;top:384px;font-size:12.5px;line-height:32px}
.contact-row{position:absolute;left:852px;display:flex;align-items:center;gap:14px;font-size:12.5px;line-height:24px}
.contact-row .ic{width:30px;height:30px;border-radius:50%;background:#fff;display:flex;align-items:center;justify-content:center;flex:none}
</style>
</head>
<body>

<!-- Top bar -->
<div class="topbar">
  <svg class="abs" style="left:122px;top:14px" width="16" height="22" viewBox="0 0 16 22"><path d="M8 0C3.6 0 0 3.5 0 7.9 0 13.5 8 22 8 22s8-8.5 8-14.1C16 3.5 12.4 0 8 0z" fill="#fff"/><circle cx="8" cy="8" r="3" fill="#8b0000"/></svg>
  <span class="abs" style="left:156px;top:20px">48 Larkin Road, Ashbury</span>
  <span class="abs" style="left:843px;top:20px">Follow Us On:</span>
  <span class="social" style="left:937px;top:11px"></span>
  <span class="social" style="left:974px;top:11px"></span>
  <span class="social" style="left:1011px;top:11px"></span>
  <span class="social" style="left:1050px;top:11px"></span>
</div>

<!-- Navigation -->
<nav class="nav">
  <a class="active" style="left:120px">Home</a>
  <a style="left:222px">About Us</a>
  <a style="left:346px">Our Trailers</a>
  <a style="left:739px">Custom Made Trailers</a>
  <a style="left:930px">Blog</a>
  <a style="left:1006px">Contact Us</a>
</nav>
<div class="logo-box"><span class="mark"></span><span class="name">KEYSTONE HAUL</span></div>

<!-- Hero -->
<section class="hero">
  <span class="abs" style="left:49px;top:116px;width:2px;height:378px;background:var(--red)"></span>
  <svg class="abs" style="left:38px;top:293px" width="24" height="34" viewBox="0 0 24 34"><rect x="1" y="1" width="22" height="32" rx="11" fill="var(--red)"/><line x1="1" y1="16" x2="23" y2="16" stroke="#fff" stroke-width="2"/><line x1="12" y1="4" x2="12" y2="12" stroke="#fff" stroke-width="2"/></svg>
  <h1><b>Custom</b> Trailers<br>For Diesel<br>Dominance.</h1>
  <p class="body abs" style="left:120px;top:300px;width:330px">Lorem Ipsum is simply dummy text of the printing and typesetting industry.</p>
  <a class="btn" style="left:120px;top:377px;width:146px;height:38px">Learn More</a>
  <div class="photo" role="img" aria-label="Red diesel semi truck with white trailer" style="left:528px;top:55px;width:672px;height:482px;background:radial-gradient(ellipse at 45% 55%,#c4161c 0%,#9a0f14 35%,#d9d9d9 62%,var(--panel) 75%)"></div>
</section>

<!-- About -->
<section>
  <div class="photo" role="img" aria-label="Row of trucks parked under a cloudy sky" style="left:120px;top:820px;width:469px;height:452px;background:linear-gradient(180deg,#a9c6e0 0%,#dfe7ee 45%,#8b8e93 70%,#6c6e70 100%)"></div>
  <div class="photo" role="img" aria-label="Trucks at a depot" style="left:120px;top:1120px;width:152px;height:152px;background:linear-gradient(180deg,#8a99a8,#4d4a45);border:5px solid var(--red);border-left:none;border-bottom:none"></div>
  <h2 class="section-title" style="left:648px;top:852px"><b>About</b> Keystone Haul</h2>
  <p class="body abs" style="left:648px;top:910px;width:436px">Lorem Ipsum is simply dummy text of the printing and typesetting industry. Lorem Ipsum has been the industry's standard dummy text ever since the 1500s, when an unknown printer took a galley of type and scrambled it to make a type specimen book. It has survived not only five centuries, but also the leap into electronic typesetting, remaining essentially unchanged.</p>
  <p class="body abs" style="left:648px;top:1090px;width:436px">Lorem Ipsum is simply dummy text of the printing and typesetting industry. Lorem Ipsum has been the industry's standard dummy text ever since the 1500s,</p>
  <a class="btn" style="left:648px;top:1196px;width:146px;height:34px">Read More</a>
</section>

<!-- Why -->
<section class="abs" style="left:0;top:1385px;width:1200px;height:737px;background:var(--panel)">
  <h2 class="section-title" style="left:120px;top:154px"><b>Why</b> Keystone Haul</h2>
  <p class="body abs" style="left:120px;top:212px;width:390px">Lorem Ipsum is simply dummy text of the printing and typesetting industry. Lorem Ipsum has been the industry's standard dummy text ever since the 1500s,</p>
  <p class="body abs" style="left:120px;top:314px;width:390px">Lorem Ipsum is simply dummy text of the printing and typesetting industry.</p>
  <div class="bar-row" style="top:404px"><span>Lorem Ipsum</span><span class="val" style="left:288px">75%</span><span class="track"></span><span class="fill" style="width:320px"></span><span class="dot" style="left:315px"></span></div>
  <div class="bar-row" style="top:460px"><span>Lorem Ipsum</span><span class="val" style="left:342px">85%</span><span class="track"></span><span class="fill" style="width:374px"></span><span class="dot" style="left:369px"></span></div>
  <div class="bar-row" style="top:515px"><span>Lorem Ipsum</span><span class="val" style="left:366px">90%</span><span class="track"></span><span class="fill" style="width:398px"></span><span class="dot" style="left:393px"></span></div>
  <span class="abs" style="left:970px;top:96px;width:124px;height:139px;background:var(--red)"></span>
  <span class="abs" style="left:594px;top:504px;width:126px;height:135px;background:var(--red)"></span>
  <div class="photo" role="img" aria-label="Red truck with box trailer at sunset" style="left:611px;top:111px;width:469px;height:513px;background:linear-gradient(160deg,#3a4a55 0%,#b3141b 40%,#8c0f12 60%,#b58f6a 85%,#7a5b43 100%)"></div>
</section>

<!-- Special Trailers -->
<section>
  <h2 class="section-title" style="left:0;width:1200px;text-align:center;top:2227px"><b>Our</b> Special Trailers</h2>
  <div class="trailer-card" style="left:120px;box-shadow:0 8px 22px rgba(0,0,0,.1)">
    <div role="img" aria-label="Flatbed lowboy trailer" style="position:absolute;left:40px;top:140px;width:224px;height:40px;background:linear-gradient(180deg,#e0e0e0,#7a7a7a)"></div>
  </div>
  <a class="btn" style="left:193px;top:2617px;width:152px;height:35px">Explore Now</a>
  <div class="trailer-card" style="left:448px;border:1px solid var(--red-bright)">
    <div role="img" aria-label="Red dump trailer truck" style="position:absolute;left:26px;top:60px;width:250px;height:180px;background:linear-gradient(135deg,#c81e26,#8e8e8e)"></div>
  </div>
  <div class="trailer-card" style="left:776px;border:1px solid var(--red-bright)">
    <div role="img" aria-label="Gooseneck lowboy trailer" style="position:absolute;left:36px;top:136px;width:232px;height:44px;background:linear-gradient(180deg,#c9b28a,#2b2b2b)"></div>
  </div>
</section>

<!-- Testimonials -->
<section class="abs" style="left:0;top:2765px;width:1200px;height:546px;background:var(--panel);overflow:hidden">
  <h2 class="section-title" style="left:120px;top:106px"><b>Our</b> Testimonials</h2>
  <span class="abs" style="left:970px;top:104px;width:46px;height:46px;border-radius:50%;border:1.5px solid var(--red-bright)"></span>
  <svg class="abs" style="left:987px;top:120px" width="12" height="14" viewBox="0 0 12 14"><path d="M8 2 3 7l5 5" fill="none" stroke="var(--red)" stroke-width="2"/></svg>
  <span class="abs" style="left:1033px;top:104px;width:46px;height:46px;border-radius:50%;background:var(--red)"></span>
  <svg class="abs" style="left:1050px;top:120px" width="12" height="14" viewBox="0 0 12 14"><path d="M4 2l5 5-5 5" fill="none" stroke="#fff" stroke-width="2"/></svg>

  <div class="t-card" style="left:120px;top:226px"><span class="quote">”</span><p>It was popularised in the 1960s with the release of Letraset sheets containing Lorem Ipsum passages, and more recently with desktop publishing software.</p><span class="who">DANA MERROW</span><span class="avatar" role="img" aria-label="Customer portrait" style="background:linear-gradient(135deg,#c0392b,#5a2a1e)"></span></div>
  <div class="t-card" style="left:593px;top:226px"><span class="quote">”</span><p>It was popularised in the 1960s with the release of Letraset sheets containing Lorem Ipsum passages, and more recently with desktop publishing software.</p><span class="who">DANA MERROW</span><span class="avatar" role="img" aria-label="Customer portrait" style="background:linear-gradient(135deg,#f0b429,#2f6db5)"></span></div>
  <div class="t-card" style="left:1067px;top:226px"><p>It was popularised in the 1960s with the release of Letraset sheets containing Lorem Ipsum passages, and more recently with desktop publishing software.</p><span class="avatar" role="img" aria-label="Customer portrait" style="background:linear-gradient(135deg,#e8d9c2,#c9a055)"></span></div>
</section>

<!-- Blog -->
<section>
  <h2 class="section-title" style="left:0;width:1200px;text-align:center;top:3416px"><b>Our</b> Blog</h2>
  <article class="blog-card" style="left:133px;box-shadow:0 8px 22px rgba(0,0,0,.12)">
    <div class="img" role="img" aria-label="Truck among shipping containers from above" style="background:linear-gradient(135deg,#6d7f86,#b4583c 50%,#3f6f8f)"></div>
    <div class="date">Aug 11, 2018</div><h3>Five Ways That Can Develop Your Business</h3><p>Lorem Ipsum is simply dummy text of the printing and typesetting industry.</p><div class="more">Read More ›</div>
  </article>
  <article class="blog-card" style="left:461px;border:1px solid var(--red-bright);border-top:none">
    <div class="img" role="img" aria-label="Red semi truck in a yard" style="background:linear-gradient(180deg,#a9c4dc,#b3141b 55%,#555)"></div>
    <div class="date">Aug 11, 2018</div><h3>Five Ways That Can Develop Your Business</h3><p>Lorem Ipsum is simply dummy text of the printing and typesetting industry.</p><div class="more">Read More ›</div>
  </article>
  <article class="blog-card" style="left:789px;border:1px solid var(--red-bright);border-top:none">
    <div class="img" role="img" aria-label="Cargo truck on a road at sunrise" style="background:linear-gradient(135deg,#f3e1b5,#8a7a55 55%,#3c3a35)"></div>
    <div class="date">Aug 11, 2018</div><h3>Five Ways That Can Develop Your Business</h3><p>Lorem Ipsum is simply dummy text of the printing and typesetting industry.</p><div class="more">Read More ›</div>
  </article>
</section>

<!-- Footer -->
<footer class="footer">
  <div class="logo-box" style="top:120px"><span class="mark"></span><span class="name">KEYSTONE HAUL</span></div>
  <h4 style="left:143px">About Us</h4>
  <p class="abs" style="left:143px;top:384px;width:225px;font-size:12.5px;line-height:24px">Lorem Ipsum is simply dummy text of the printing and typesetting industry. Lorem Ipsum has been the industry's standard dummy text ever since the 1500s,</p>
  <span class="divider" style="left:443px"></span>
  <h4 style="left:533px">Quick Links</h4>
  <ul><li>Home</li><li>About Us</li><li>Our Trailers</li><li>Custom Made trailers</li><li>Our Blog</li><li>Contact Us</li></ul>
  <span class="divider" style="left:761px"></span>
  <h4 style="left:852px">Contact Us</h4>
  <div class="contact-row" style="top:391px"><span class="ic"><svg width="14" height="14" viewBox="0 0 14 14"><path d="M3 1l2 3-1.5 1.5a8 8 0 0 0 5 5L10 9l3 2-1 2.5C6 13 1 8 .5 2z" fill="var(--red)"/></svg></span>555-014-2290</div>
  <div class="contact-row" style="top:448px"><span class="ic"><svg width="14" height="10" viewBox="0 0 14 10"><rect width="14" height="10" fill="var(--red)"/><path d="M0 0l7 5 7-5" fill="none" stroke="#fff"/></svg></span>hello@keystonehaul.com</div>
  <div class="contact-row" style="top:508px"><span class="ic"><svg width="10" height="14" viewBox="0 0 16 22"><path d="M8 0C3.6 0 0 3.5 0 7.9 0 13.5 8 22 8 22s8-8.5 8-14.1C16 3.5 12.4 0 8 0z" fill="var(--red)"/><circle cx="8" cy="8" r="3" fill="#fff"/></svg></span>12B Orchard Lane,<br>Fairview 4410</div>
  <span class="abs" style="left:39px;top:630px;width:1122px;height:1px;background:#666"></span>
  <p class="abs" style="left:135px;top:674px;font-size:12px">© Copyright 2023 <b>Keystone Haul</b> . All Rights Reserved</p>
  <span class="social" style="left:971px;top:661px;width:40px;height:40px"></span>
  <span class="social" style="left:1026px;top:661px;width:40px;height:40px"></span>
</footer>

</body>
</html>
```